Wall Sticker (3 design options)

We need 3 design options for wall sticker design, taking inspiration from the Roll-Up Banner PDF files. The wall sticker will promote our school's courses and qualifications.

Size of wall sticker: 2400 mm (height) x 900 mm (width)

Wall sticker will be installed next to our classroom entrance (refer to photo of wall - file name: BRVKM Wall & Glass Panel Size.jpg

Background on our business (for your own knowledge): Our company is called Loomcraft and Apparel Skills Institute (LASKI). We help train the fashion industry as well as people who are interested in joining the fashion industry.

Must Have:
- Take colour scheme from uploaded PDF files
- Hex code for corporate colour is #DA291C (Red)
- Other Corporate Colours to be Included: Grey, White, Black

Font Type to be used: Frutiger

Logos to be used are attached: LASKI logo, PQN DLH logo, and LearnMark logo

=======================================================
This is the text content for the wall sticker:

STEP INTO THE WORLD OF FASHION

PROFESSIONAL PQN SHORT COURSES
- Fashion Styling
- Sewing and Alteration
- Leather Care
- Fabric Care

PQN ADVANCED CERTIFICATE IN FASHION TECHNOLOGY
• Apparel Design and Product Development
• Merchandising and Marketing

PQN DIPLOMA IN FASHION TECHNOLOGY:
• Footwear Design and Product Development

FUNDING & CAREER OPPORTUNITIES
Speak to us today about your eligibility in funding and potential career opportunities upon graduation.

Tel: 64829305
Email: enquiry@lasinst-mail.org
Website: www.lasinst-web.edu.sg

Stock photo: please propose stock photos for the 3 design options. The photo should 'speak' about fashion in general but not specifically on sewing, footwear making, etc but should be generic. Please do not use runway photos or photos that have fashion illustrations.

FINAL ARTWORK requirements:
- Source file format: saved for Adobe Illustrator CS6 (ai), not locked so that we can make edits in future
- Print file format: PDF (editable and not locked), must include crop marks and 3 mm bleed.

Target Market(s)

General Public, Fashionistas, Fashion Students, Aspiring Footwear Enthusiasts and people interested to enter the fashion industry

Font styles to use
Sans Serif
Other font styles liked:
• Frutiger

Colors
ec1f27
ffffff
000000
757575
c5c5c5

Requirements
Must have
• - Hex code for corporate colour is #DA291C (Red)
• - Other Corporate Colours to be Included: Grey, White, Black
• Please put in the header (at the top): LASKI logo
• Please put somewhere in the footer (bottom):
• - PQN DLH logo
• - LearnMark logo
• - our contact details and website - telephone: 64829305, email: enquiry@lasinst-mail.org, and website: www.lasinst-web.edu.sg
Should not have
• stock photo with fashion illustration

```html
<!DOCTYPE html>
<html lang="en">
<head>
<meta charset="utf-8">
<title>LASKI – Wall Sticker Options</title>
<link rel="stylesheet" href="https://fonts.googleapis.com/css2?family=Hind:wght@400;500&display=swap">
<style>
  :root {
    --red: #da291c;
    --black: #000000;
    --white: #ffffff;
    --grey-dark: #757575;
    --grey-mid: #c5c5c5;
    --grey-light: #dde0e0;
    --ink: #1a1a1a;
    --font: "Hind", "Frutiger", Arial, sans-serif;
  }
  * { box-sizing: border-box; margin: 0; padding: 0; }
  html, body { width: 1200px; height: 876px; overflow: hidden; background: var(--white); }
  body { position: relative; font-family: var(--font); color: var(--ink); }

  .option { position: absolute; top: 0; width: 327px; height: 872px; overflow: hidden; }
  .option--one   { left: 185px; background: var(--grey-light); }
  .option--two   { left: 514px; background: var(--white); }
  .option--three { left: 844px; background: var(--grey-light); }

  .backdrop { position: absolute; inset: 0; width: 327px; height: 872px; }

  .brand {
    position: absolute; top: 20px; right: 46px;
    font-family: var(--font); font-weight: 400; font-size: 40px;
    letter-spacing: 1px; color: var(--black); line-height: 1;
  }

  .headline {
    position: absolute; left: 18px; right: 6px;
    color: var(--red); font-weight: 400; font-size: 28.5px;
    line-height: 32px; letter-spacing: 0.3px;
  }

  .courses { position: absolute; left: 18px; right: 4px; font-size: 11.2px; line-height: 12.8px; }
  .courses section + section { margin-top: 15px; }
  .courses h3 { font-weight: 400; font-size: 11.2px; text-transform: uppercase; letter-spacing: 0.1px; white-space: nowrap; }
  .courses ul { list-style: none; margin-top: 5px; padding-left: 8.5px; }
  .courses li { white-space: nowrap; }
  .courses p { margin-top: 5px; padding-left: 8.5px; white-space: nowrap; }

  .contact {
    position: absolute; left: 6px; color: var(--white);
    font-size: 7.4px; line-height: 9.6px; font-style: normal;
  }

  .accreditation { position: absolute; width: 130px; height: 50px; }
  .accreditation .cert {
    position: absolute; left: 69px; top: 33px;
    font-size: 3.6px; line-height: 4.4px; color: var(--ink); white-space: nowrap;
  }
</style>
</head>
<body>

<article class="option option--one">
  <svg class="backdrop" viewBox="0 0 327 872">
    <defs>
      <linearGradient id="photoToneA" x1="0" y1="0" x2="1" y2="1">
        <stop offset="0" stop-color="#eeeae4"/>
        <stop offset="0.5" stop-color="#e6d3c9"/>
        <stop offset="1" stop-color="#cfc6c2"/>
      </linearGradient>
    </defs>
    <polygon points="150,0 327,0 327,74" fill="#ececec"/>
    <polygon points="327,74 327,130 220,100" fill="var(--grey-mid)"/>
    <polygon role="img" aria-label="Stock photo: smiling fashion professional in a bright studio with clothing racks" points="0,36 327,134 327,398 0,300" fill="url(#photoToneA)"/>
    <line x1="0" y1="36" x2="327" y2="134" stroke="var(--black)" stroke-width="4"/>
    <line x1="0" y1="300" x2="327" y2="398" stroke="var(--black)" stroke-width="4"/>
    <polygon points="0,302 260,380 0,368" fill="var(--grey-mid)"/>
    <polygon points="327,760 167,818 327,872" fill="var(--white)"/>
    <polygon points="0,774 167,818 0,872" fill="var(--red)"/>
  </svg>
  <div class="brand">LASKI</div>
  <h1 class="headline" style="top:408px">STEP INTO THE WORLD OF FASHION</h1>
  <div class="courses" style="top:494px">
    <section><h3>Professional PQN Short Courses</h3>
      <ul><li>Fashion Styling</li><li>Sewing and Alteration</li><li>Leather Care</li><li>Fabric Care</li></ul></section>
    <section><h3>PQN Advanced Certificate in Fashion Technology</h3>
      <ul><li>Apparel Design and Product Development</li><li>Merchandising and Marketing</li></ul></section>
    <section><h3>PQN Diploma in Fashion Technology:</h3>
      <ul><li>Apparel Design and Product Development</li><li>Merchandising and Marketing</li><li>Footwear Design and Product Development</li></ul></section>
    <section><h3>Funding &amp; Career Opportunities</h3>
      <p>Speak to us today about your eligibility in funding<br>and potential career opportunities upon graduation.</p></section>
  </div>
  <address class="contact" style="top:808px">Tel: 64829305<br>Email: enquiry@lasinst-mail.org<br>Website: www.lasinst-web.edu.sg</address>
  <div class="accreditation" style="left:177px; top:812px">
    <svg width="130" height="50" viewBox="0 0 130 50" aria-label="DLH and LearnMark partner marks" role="img">
      <rect x="0.5" y="8.5" width="55" height="22" rx="2" fill="var(--white)" stroke="var(--grey-mid)"/>
      <circle cx="69" cy="17" r="15" fill="var(--red)"/>
      <rect x="84" y="10" width="30" height="12" rx="2" fill="var(--grey-dark)"/>
    </svg>
    <div class="cert">Cert No.: LM-4-7712<br>Validity: 01/2024 - 12/2027</div>
  </div>
</article>

<article class="option option--two">
  <svg class="backdrop" viewBox="0 0 327 872">
    <defs>
      <linearGradient id="photoToneB" x1="0" y1="0" x2="1" y2="1">
        <stop offset="0" stop-color="#f0ece6"/>
        <stop offset="0.5" stop-color="#e6d3c9"/>
        <stop offset="1" stop-color="#d2c8c3"/>
      </linearGradient>
    </defs>
    <rect x="0" y="0" width="327" height="122" fill="var(--grey-mid)"/>
    <polygon points="85,0 327,0 242,122" fill="var(--white)"/>
    <polygon points="327,8 327,122 242,122" fill="var(--grey-light)"/>
    <rect x="0" y="122" width="327" height="5" fill="var(--black)"/>
    <rect role="img" aria-label="Stock photo: smiling fashion professional in a bright studio with clothing racks" x="0" y="127" width="327" height="271" fill="url(#photoToneB)"/>
    <rect x="0" y="398" width="327" height="5" fill="var(--black)"/>
    <polygon points="327,740 105,872 327,872" fill="var(--grey-light)"/>
    <polygon points="0,740 190,816 0,872" fill="var(--red)"/>
  </svg>
  <div class="brand">LASKI</div>
  <h1 class="headline" style="top:416px">STEP INTO THE WORLD OF FASHION</h1>
  <div class="courses" style="top:489px">
    <section><h3>Professional PQN Short Courses</h3>
      <ul><li>Fashion Styling</li><li>Sewing and Alteration</li><li>Leather Care</li><li>Fabric Care</li></ul></section>
    <section><h3>PQN Advanced Certificate in Fashion Technology</h3>
      <ul><li>Apparel Design and Product Development</li><li>Merchandising and Marketing</li></ul></section>
    <section><h3>PQN Diploma in Fashion Technology:</h3>
      <ul><li>Apparel Design and Product Development</li><li>Merchandising and Marketing</li><li>Footwear Design and Product Development</li></ul></section>
    <section><h3>Funding &amp; Career Opportunities</h3>
      <p>Speak to us today about your eligibility in funding<br>and potential career opportunities upon graduation.</p></section>
  </div>
  <address class="contact" style="top:808px">Tel: 64829305<br>Email: enquiry@lasinst-mail.org<br>Website: www.lasinst-web.edu.sg</address>
  <div class="accreditation" style="left:178px; top:812px">
    <svg width="130" height="50" viewBox="0 0 130 50" aria-label="DLH and LearnMark partner marks" role="img">
      <rect x="0.5" y="8.5" width="55" height="22" rx="2" fill="var(--white)" stroke="var(--grey-mid)"/>
      <circle cx="69" cy="17" r="15" fill="var(--red)"/>
      <rect x="84" y="10" width="30" height="12" rx="2" fill="var(--grey-dark)"/>
    </svg>
    <div class="cert">Cert No.: LM-4-7712<br>Validity: 01/2024 - 12/2027</div>
  </div>
</article>

<article class="option option--three">
  <svg class="backdrop" viewBox="0 0 327 872">
    <defs>
      <linearGradient id="photoToneC" x1="0" y1="0" x2="1" y2="1">
        <stop offset="0" stop-color="#efebe5"/>
        <stop offset="0.5" stop-color="#e6d3c9"/>
        <stop offset="1" stop-color="#d0c7c2"/>
      </linearGradient>
    </defs>
    <rect role="img" aria-label="Stock photo: smiling fashion professional in a bright studio with clothing racks" x="0" y="140" width="327" height="276" fill="url(#photoToneC)"/>
    <polygon points="0,0 327,132 0,164" fill="var(--grey-mid)"/>
    <polygon points="0,0 327,0 327,132" fill="var(--grey-light)"/>
    <polygon points="0,352 140,416 0,416" fill="var(--white)"/>
    <polygon points="327,556 250,620 327,680" fill="var(--white)" opacity="0.7"/>
    <polygon points="327,772 220,872 327,872" fill="var(--white)"/>
    <polygon points="0,752 185,872 0,872" fill="var(--red)"/>
  </svg>
  <div class="brand">LASKI</div>
  <h1 class="headline" style="top:422px">STEP INTO THE WORLD OF FASHION</h1>
  <div class="courses" style="top:509px">
    <section><h3>Professional PQN Short Courses</h3>
      <ul><li>Fashion Styling</li><li>Sewing and Alteration</li><li>Leather Care</li><li>Fabric Care</li></ul></section>
    <section><h3>PQN Advanced Certificate in Fashion Technology</h3>
      <ul><li>Apparel Design and Product Development</li><li>Merchandising and Marketing</li></ul></section>
    <section><h3>PQN Diploma in Fashion Technology:</h3>
      <ul><li>Apparel Design and Product Development</li><li>Merchandising and Marketing</li><li>Footwear Design and Product Development</li></ul></section>
    <section><h3>Funding &amp; Career Opportunities</h3>
      <p>Speak to us today about your eligibility in funding<br>and potential career opportunities upon graduation.</p></section>
  </div>
  <address class="contact" style="top:810px">Tel: 64829305<br>Email: enquiry@lasinst-mail.org<br>Website: www.lasinst-web.edu.sg</address>
  <div class="accreditation" style="left:180px; top:814px">
    <svg width="130" height="50" viewBox="0 0 130 50" aria-label="DLH and LearnMark partner marks" role="img">
      <rect x="0.5" y="8.5" width="55" height="22" rx="2" fill="var(--white)" stroke="var(--grey-mid)"/>
      <circle cx="84" cy="18" r="15" fill="var(--red)"/>
      <rect x="99" y="11" width="28" height="12" rx="2" fill="var(--grey-dark)"/>
    </svg>
    <div class="cert" style="left:84px">Cert No.: LM-4-7712<br>Validity: 01/2024 - 12/2027</div>
  </div>
</article>

</body>
</html>
```